Mobile Money & Fintech Solutions needs a business card design and logo

I need the design of a business card and a logo for my consultant, based in Asuncion Paraguay. I am in the Digital World category, specializing in Mobile Money, Fintech Solutions & e-commerce. I would like the design to reflect trust and above all encompass the area of ​​specialty of the services that I offer. (Mobile Money, Fintech Solutions & e-commerce)

Target Market(s)

Financial entities, companies wishing to undertake a Fintech or e-commerce project

Contact Information for Business Card

Marisol Quenderra
Senior Advisory Consultant
Cel +595982417305
Skype ID marisolquenderra
Linkedin: http://lnkvo.example/7wqpzjT

Logo Text

Fintech Solutions&E-commerce

Requirements
Must have
• I would like it to be a fusion of symbols, example of the @, the $, cellular (cell) that can encompass the areas.
Nice to have
• Must be related to the Fintech area and / or Mobile MOney and e-commerce. It is a new consultancy, so there are no previous logos

```html
<!DOCTYPE html>
<html lang="en">
<head>
<meta charset="utf-8">
<title>Kavira Digital – Business Card</title>
<link href="https://fonts.googleapis.com/css2?family=Lato:wght@400;700&display=swap" rel="stylesheet">
<style>
  :root {
    --bg: #2b2b2d;
    --card-dark-a: #1c1c1d;
    --card-dark-b: #3a3a3c;
    --orange: #ff6a00;
    --ink: #1e1e1e;
    --grey: #58585a;
    --white: #ffffff;
    --strip: #2e2e30;
  }
  * { margin: 0; padding: 0; box-sizing: border-box; }
  html, body { width: 1200px; height: 900px; overflow: hidden; }
  body {
    background: var(--bg);
    font-family: "Lato", sans-serif;
    position: relative;
  }
  .card {
    position: absolute;
    left: 280px;
    width: 640px;
    height: 366px;
    overflow: hidden;
    box-shadow: 0 14px 30px rgba(0,0,0,.45);
  }
  .card--front {
    top: 64px;
    background: radial-gradient(ellipse at 40% 30%, var(--card-dark-b), var(--card-dark-a) 75%);
    color: var(--white);
  }
  .card--back {
    top: 470px;
    background: var(--white);
    color: var(--ink);
  }

  /* brand lockup */
  .brand { position: absolute; display: flex; align-items: center; gap: 16px; }
  .brand__square { width: 34px; height: 34px; background: var(--orange); }
  .brand__name { font-weight: 700; letter-spacing: .5px; line-height: 1; }
  .card--front .brand { left: 50%; top: 118px; transform: translateX(-50%); }
  .card--front .brand__name { font-size: 46px; color: var(--white); white-space: nowrap; }
  .card--back .brand { left: 56px; top: 50px; }
  .card--back .brand__name { font-size: 40px; color: var(--grey); white-space: nowrap; }

  .tagline {
    position: absolute; left: 0; right: 0; top: 240px;
    text-align: center; font-size: 15px; letter-spacing: 1px; text-transform: uppercase;
  }
  .tagline__dot { display: inline-block; width: 6px; height: 6px; border-radius: 50%; background: var(--orange); margin: 0 8px 3px; vertical-align: middle; }

  .rule { position: absolute; left: 48px; right: 46px; top: 176px; height: 2px; background: var(--orange); }

  .contact { position: absolute; left: 48px; top: 192px; list-style: none; font-size: 17px; }
  .contact li { display: flex; align-items: center; gap: 10px; height: 26px; }
  .contact svg { width: 16px; height: 16px; fill: var(--orange); flex: none; }

  .person { position: absolute; right: 46px; top: 188px; text-align: right; }
  .person__name { font-size: 27px; line-height: 32px; font-weight: 700; color: var(--orange); }
  .person__role { font-size: 17px; line-height: 22px; }

  .address { position: absolute; right: 50px; top: 254px; text-align: right; font-size: 18px; line-height: 22px; }

  .foot-strip { position: absolute; left: 0; right: 0; bottom: 0; height: 14px; background: var(--strip); }
  .web-tab { position: absolute; left: 228px; bottom: 14px; width: 372px; height: 34px; }
  .web-tab svg { position: absolute; inset: 0; }
  .web-tab__text { position: relative; display: block; text-align: center; line-height: 34px; font-size: 17px; color: var(--white); letter-spacing: .5px; }
</style>
</head>
<body>

<section class="card card--front">
  <div class="brand">
    <span class="brand__square"></span>
    <span class="brand__name">Kavira Digital</span>
  </div>
  <p class="tagline">Mobile Money<span class="tagline__dot"></span>Fintech Solutions<span class="tagline__dot"></span>E-Commerce</p>
</section>

<section class="card card--back">
  <div class="brand">
    <span class="brand__square"></span>
    <span class="brand__name">Kavira Digital</span>
  </div>

  <div class="rule"></div>

  <ul class="contact">
    <li>
      <svg viewBox="0 0 16 16" aria-hidden="true"><path d="M3.6 1.2l2.3 2.6-1.2 1.8c.8 2 2.2 3.5 4.2 4.4l1.8-1.2 2.6 2.3-1.3 2.4C7 13.3 2.6 9 1.2 4z"/></svg>
      555 014 2290
    </li>
    <li>
      <svg viewBox="0 0 16 16" aria-hidden="true"><path d="M4 1h8v4H4zM1 6h14v6h-3v3H4v-3H1zm4 4v3h6v-3z"/></svg>
      555 014 2291
    </li>
    <li>
      <svg viewBox="0 0 16 16" aria-hidden="true"><path d="M1 3h14v10H1zm1.5 1.2L8 8.5l5.5-4.3z"/></svg>
      info@kaviradigital.example
    </li>
  </ul>

  <div class="person">
    <p class="person__name">Daniel Ostrova</p>
    <p class="person__role">Manager</p>
  </div>

  <p class="address">418 Linden Row<br>Harlow TX 75500</p>

  <div class="web-tab">
    <svg viewBox="0 0 372 34" preserveAspectRatio="none" aria-hidden="true">
      <path d="M0 34 L22 6 Q26 0 34 0 L372 0 L346 34 Z" fill="var(--orange)"/>
    </svg>
    <span class="web-tab__text">www.kaviradigital.example</span>
  </div>
  <div class="foot-strip"></div>
</section>

</body>
</html>
```